Company: Plant Grillhouse
We make Plant Grillhouse more popular.
We are producing cooking books and spices.
For our spices (5 sorts) we need an label design.
Measurments of the label: 255mm x 55mm ( small changes of the exact measurements could follow in the next few days)
Name of the sorts:
- Sunny Zestpepper (Yellow)
- Desert Caravan (Orange/Brown)
- Charred Ember-Rub (Red)
- Charm of Tuscany (Green)
- Bold Shallotine (Black)
Attached you can find our main brand.
You can see we try to be clean and simple.
The package is a square glass with a cork closure
4 Side.
Side 1: Logo and Spice Name
Side 2: Incredients and Company Information
Side 3: Nice grphic that matches the sort of the spice
Side 4: Short story of the product and its added value
We look forward to cool suggestions.
Regards
Tobias
We want make the vegan lifestyle more cool.
So therefore don`t choose a too much ecological way, that is not up to date.

```html
<!DOCTYPE html>
<html lang="de">
<head>
<meta charset="utf-8">
<title>Bold Shallotine – Gewürzetikett</title>
<link rel="stylesheet" href="https://fonts.googleapis.com/css2?family=Oswald:wght@600&family=Montserrat:wght@400;700&display=swap">
<style>
  :root {
    --label-grey: #d9d9d9;
    --ink: #111111;
    --band-black: #000000;
    --divider: #ffffff;
    --art-dark: #8a8a8a;
    --art-light: #c4c4c4;
    --logo-text: #ffffff;
  }
  * { margin: 0; padding: 0; box-sizing: border-box; }
  html, body { width: 1200px; height: 259px; overflow: hidden; background: var(--divider); }
  .label {
    position: relative;
    width: 1200px;
    height: 259px;
    font-family: "Montserrat", sans-serif;
    color: var(--ink);
  }
  .label__main {
    position: absolute; left: 0; top: 0;
    width: 1200px; height: 207px;
    background: var(--label-grey);
  }
  .label__band {
    position: absolute; left: 0; top: 210px;
    width: 1200px; height: 49px;
    background: var(--band-black);
  }
  .herb-art {
    position: absolute; left: 0; top: 0;
    width: 376px; height: 207px;
    background: linear-gradient(135deg, var(--art-light), var(--art-dark) 55%, var(--art-light));
  }
  .herb-art--edge {
    left: 1170px; top: 36px; width: 30px; height: 104px;
    border-radius: 40px 0 0 40px;
  }
  .spice-name {
    position: absolute; left: 481px; top: 52px;
    transform: translateX(-50%);
    font-family: "Oswald", sans-serif;
    font-weight: 600;
    font-size: 50px;
    line-height: 51px;
    letter-spacing: 0.2em;
    text-align: center;
    text-transform: uppercase;
    white-space: nowrap;
  }
  .column-title {
    font-weight: 700;
    font-size: 10px;
    letter-spacing: 0.16em;
    text-transform: uppercase;
    text-align: center;
    margin-bottom: 15px;
  }
  .story {
    position: absolute; left: 649px; top: 24px;
    width: 240px;
    text-align: center;
  }
  .story__text {
    font-size: 10.4px;
    line-height: 16px;
    letter-spacing: 0.08em;
  }
  .facts {
    position: absolute; left: 971px; top: 24px;
    width: 190px;
  }
  .facts__list { list-style: none; }
  .facts__row {
    display: flex;
    font-size: 10.8px;
    line-height: 16px;
    letter-spacing: 0.1em;
    text-transform: uppercase;
  }
  .facts__leader {
    flex: 1;
    overflow: hidden;
    white-space: nowrap;
  }
  .facts__leader::after { content: "........................................"; }
  .facts__company {
    margin-top: 15px;
    font-weight: 700;
    font-size: 10.4px;
    letter-spacing: 0.14em;
    text-align: center;
    text-transform: uppercase;
  }
  .brand {
    position: absolute; left: 398px; top: 222px;
    display: flex; align-items: center; gap: 9px;
  }
  .brand__mark { width: 24px; height: 24px; border-radius: 50%; background: var(--logo-text); }
  .brand__name {
    color: var(--logo-text);
    font-weight: 700;
    font-size: 13.5px;
    letter-spacing: 0.01em;
    text-transform: uppercase;
  }
</style>
</head>
<body>
<main class="label">
  <section class="label__main">
    <div class="herb-art" role="img" aria-label="Schwarz-weiße Strichzeichnung von Basilikum, Chilischoten, Knoblauch und Rosmarin"></div>
    <div class="herb-art herb-art--edge" role="img" aria-label="Angeschnittene Basilikumblätter als Strichzeichnung"></div>

    <h1 class="spice-name">Bold<br>Shallotine</h1>

    <article class="story">
      <h2 class="column-title">Lemoncurry-Gewürz:</h2>
      <p class="story__text">Geschichte des Gewürzes. Lorem ipsum dolor sit amet, consetetur sadipscing elitr, sed diam nonumy eirmod tempor invidunt ut labore et dolore magna aliquyam erat, sed diam voluptua.<br>sed diam nonumy eirmod tempor invidunt ut magna aliquyam erat, sed diam voluptua</p>
    </article>

    <aside class="facts">
      <h2 class="column-title">Inhaltsstoffe:</h2>
      <ul class="facts__list">
        <li class="facts__row"><span>Energie</span><span class="facts__leader"></span><span>kJ/kcal</span></li>
        <li class="facts__row"><span>Fett</span><span class="facts__leader"></span><span>g</span></li>
        <li class="facts__row"><span>Kohlenhydrate</span><span class="facts__leader"></span><span>g</span></li>
        <li class="facts__row"><span>davon Zucker</span><span class="facts__leader"></span><span>g</span></li>
        <li class="facts__row"><span>Ballaststoffe</span><span class="facts__leader"></span><span>g</span></li>
        <li class="facts__row"><span>Eiweiß</span><span class="facts__leader"></span><span>g</span></li>
        <li class="facts__row"><span>Salz</span><span class="facts__leader"></span><span>g</span></li>
      </ul>
      <p class="facts__company">Plant Grillhouse GmbH</p>
    </aside>
  </section>

  <footer class="label__band">
  </footer>
  <div class="brand">
    <span class="brand__mark" aria-hidden="true"></span>
    <span class="brand__name">Plant Grillhouse</span>
  </div>
</main>
</body>
</html>
```